Home Improvement Company in need of a "Banner & Billboard Design"

I'm Looking for a Banner design 4X6 With Company Logo, Phone Number, website, Credentials and services.. I picture a charcoal/matte background i also want to look like a house shape design i will upload the sample...

I'm looking for a Billboard design to target homeowners who need Roofing Services. I need logo, number, website, KLN, Credentials and a catchy title. i will like to use the same colors for branding

Target Market(s)

Homeowners, Investors,

Industry/Entity Type

Home Improvement

Font styles to use
Decorative

Colors
00a990
5c5c5c
333333

Requirements
Must have
• All Credentials, Phone number, website, logo, logo colors, services, Eye Catchy, Direct Message, Friendly feeling,
• (555) 319 - 4826
• Roofing Gutters Painting Pressure Washing Exterior Design
Nice to have
• A catchy title, A direct message to a homeowner looking for home improvement services. noticeable
Should not have
• not Busy, no

```html
<!DOCTYPE html>
<html lang="en">
<head>
<meta charset="utf-8">
<title>Ridgeline Home Exteriors — Billboard</title>
<link rel="stylesheet" href="https://fonts.googleapis.com/css2?family=Open+Sans:wght@800&display=swap">
<style>
  :root {
    --teal: #1a9686;
    --charcoal: #333333;
    --slate: #5c5c5c;
    --paper: #ffffff;
    --backdrop: #eef0f0;
    --badge-red: #d8222a;
    --badge-blue: #1f5aa6;
  }
  html, body {
    margin: 0;
    width: 1200px;
    height: 1037px;
    overflow: hidden;
    background: var(--backdrop);
  }
  .billboard {
    position: absolute;
    left: 40px;
    top: 218px;
    width: 1120px;
    height: 600px;
    box-shadow: 0 10px 30px rgba(0,0,0,.18);
  }
  .billboard svg { display: block; }
  .service { font-family: "Open Sans", sans-serif; font-weight: 800; font-size: 30px; letter-spacing: 1.5px; fill: var(--paper); }
  .chevron { font-family: "Open Sans", sans-serif; font-weight: 800; font-size: 30px; fill: var(--teal); }
  .phone { font-family: "Open Sans", sans-serif; font-weight: 800; font-size: 88px; fill: var(--paper); }
  .website { font-family: "Open Sans", sans-serif; font-weight: 800; font-size: 58px; fill: var(--paper); }
  .brand-name { font-family: "Open Sans", sans-serif; font-weight: 800; font-size: 36px; fill: var(--teal); }
</style>
</head>
<body>
<main class="billboard">
  <svg width="1120" height="600" viewBox="0 0 1120 600" xmlns="http://www.w3.org/2000/svg">
    <rect class="board-bg" width="1120" height="600" fill="var(--paper)"/>

    <!-- charcoal services panel -->
    <polygon class="accent-slash" points="440,120 478,112 418,395 380,402" fill="var(--slate)"/>
    <polygon class="services-panel" points="490,0 1120,0 1120,240 420,380" fill="var(--charcoal)"/>

    <!-- teal contact band -->
    <polygon class="contact-band" points="0,410 1120,225 1120,405 0,590" fill="var(--teal)"/>
    <polygon class="base-strip" points="0,590 482,511 442,600 0,600" fill="var(--charcoal)"/>
    <polygon class="base-slash" points="490,510 518,505 478,600 450,600" fill="var(--slate)"/>

    <!-- brand -->
    <g class="brand">
      <rect x="70" y="170" width="32" height="32" fill="var(--teal)"/>
      <text class="brand-name" x="114" y="200">RIDGELINE</text>
      <text class="brand-name" x="70" y="248">HOME EXTERIORS</text>
    </g>

    <!-- services -->
    <g class="services" transform="rotate(-6 540 80)">
      <text class="chevron" x="540" y="80">›</text><text class="service" x="566" y="80">ROOFING</text>
      <text class="chevron" x="540" y="124">›</text><text class="service" x="566" y="124">GUTTERS</text>
      <text class="chevron" x="540" y="168">›</text><text class="service" x="566" y="168">PAINTING</text>
      <text class="chevron" x="540" y="212">›</text><text class="service" x="566" y="212">PRESSURE WASHING</text>
      <text class="chevron" x="540" y="256">›</text><text class="service" x="566" y="256">EXTERIOR DESIGN</text>
    </g>

    <!-- contact -->
    <g class="contact" transform="rotate(-9.4 60 510)">
      <text class="phone" x="60" y="494">(555) 319 - 4826</text>
      <text class="website" x="60" y="560">RidgelineExteriors.com</text>
    </g>

    <!-- credentials -->
    <g class="credentials">
      <rect role="img" aria-label="Shieldtop certified roofing contractor badge" x="610" y="512" width="190" height="52" fill="var(--badge-red)"/>
      <rect role="img" aria-label="Shieldtop roofing partner badge" x="830" y="492" width="80" height="68" fill="var(--badge-red)"/>
      <rect role="img" aria-label="KLN accredited business badge" x="942" y="484" width="56" height="72" fill="var(--paper)" stroke="var(--badge-blue)" stroke-width="4"/>
    </g>
  </svg>
</main>
</body>
</html>
```